Garden Design Business Card Design

A business card design for garden design company called ;
ROOTED IN CLAY which has a great deal of maintenance but
wishes to promote its expertise for design in planting and garden
design, but in an informal manner.

Would love to see quite a rustic approach,very strong and innovative and taking risks on typography. Am open to ideas with
colours,as memorability is important.

Target Market(s)

General public 40/50 years in a very trendy area

Industry/Entity Type

Business

Contact Information for Business Card

ROOTED IN CLAY. Garden design and maintenance.
Peter Holcombe
Telephone 01632 960417 Mobile 07700 900382

```html
<!DOCTYPE html>
<html lang="en">
<head>
<meta charset="utf-8">
<title>Rooted in Clay – Business Card</title>
<link rel="stylesheet" href="https://fonts.googleapis.com/css2?family=Poiret+One&display=swap">
<style>
  :root {
    --page-bg: #e9e7e3;
    --card-bg: #f7f7f5;
    --frame: #c9c9c9;
    --ink: #1e1e1e;
    --ink-soft: #8c8c8c;
    --ink-faint: #a6a6a6;
    --ornament-a: #e2e2e0;
    --ornament-b: #ececea;
  }
  * { margin: 0; padding: 0; box-sizing: border-box; }
  html, body {
    width: 1200px;
    height: 918px;
    overflow: hidden;
    background: var(--page-bg);
  }
  .canvas {
    position: relative;
    width: 1200px;
    height: 918px;
    display: flex;
    align-items: center;
    justify-content: center;
  }
  .business-card {
    position: relative;
    width: 1000px;
    height: 600px;
    background: var(--card-bg);
    box-shadow: 0 6px 24px rgba(0, 0, 0, 0.12);
    overflow: hidden;
    font-family: "Poiret One", sans-serif;
  }
  .card-frame {
    position: absolute;
    inset: 22px;
    border: 3px solid var(--frame);
  }
  .ornament {
    position: absolute;
    right: 40px;
    bottom: 0;
    width: 270px;
    height: 360px;
  }
  .card-content {
    position: absolute;
    left: 80px;
    top: 62px;
  }
  .brand-name {
    font-size: 96px;
    line-height: 1;
    color: var(--ink);
    letter-spacing: 1px;
    text-transform: lowercase;
    white-space: nowrap;
  }
  .brand-tagline {
    margin-top: 4px;
    margin-left: 4px;
    font-size: 42px;
    color: var(--ink-soft);
    letter-spacing: 1px;
    white-space: nowrap;
  }
  .contact-name {
    margin-top: 30px;
    margin-left: 4px;
    font-size: 36px;
    color: var(--ink);
    font-weight: 400;
    letter-spacing: 1px;
  }
  .contact-list {
    list-style: none;
    margin-top: 10px;
    margin-left: 4px;
  }
  .contact-item {
    display: flex;
    align-items: center;
    gap: 14px;
    font-size: 30px;
    color: var(--ink-faint);
    letter-spacing: 1px;
    height: 44px;
  }
  .contact-icon {
    width: 26px;
    height: 26px;
    fill: var(--ink-faint);
  }
</style>
</head>
<body>
<main class="canvas">
  <section class="business-card">
    <div class="card-frame"></div>

    <svg class="ornament" viewBox="0 0 270 360" role="img" aria-label="Faint floral damask flourish ornament in pale grey">
      <defs>
        <linearGradient id="ornamentFill" x1="0" y1="0" x2="0" y2="1">
          <stop offset="0" stop-color="var(--ornament-b)"/>
          <stop offset="1" stop-color="var(--ornament-a)"/>
        </linearGradient>
      </defs>
      <path d="M150 0 C230 20 270 90 260 170 C255 250 240 310 250 360 L20 360 C40 300 10 250 40 190 C70 120 80 40 150 0 Z" fill="url(#ornamentFill)"/>
    </svg>

    <div class="card-content">
      <h1 class="brand-name">rooted in clay</h1>
      <p class="brand-tagline">Garden design and maintenance</p>
      <h2 class="contact-name">Peter Holcombe</h2>
      <ul class="contact-list">
        <li class="contact-item">
          <svg class="contact-icon" viewBox="0 0 24 24" aria-hidden="true">
            <path d="M2 9c0-3 4-5 10-5s10 2 10 5v1.5h-5V8.5c-1.5-.6-3.2-.9-5-.9s-3.5.3-5 .9v2H2z"/>
            <path d="M6 12l2-3h8l2 3v7H6z"/>
          </svg>
          <span>01632 960417</span>
        </li>
        <li class="contact-item">
          <svg class="contact-icon" viewBox="0 0 24 24" aria-hidden="true">
            <path d="M8 1h8a2 2 0 0 1 2 2v18a2 2 0 0 1-2 2H8a2 2 0 0 1-2-2V3a2 2 0 0 1 2-2zm0 3v12h8V4z"/>
          </svg>
          <span>07700 900382</span>
        </li>
      </ul>
    </div>
  </section>
</main>
</body>
</html>
```